Book cover design for 'Harbour Lantern' novel

Title of book 'Harbour Lantern'
Subtitle 'a Owen Tessary novel'
Author 'K L Dunmore'
Book genre 'novel - adventure'
Format ' eBook, paperback, audio, thumbnail'
Type 'Self-publishing through RVN'
Trim size 6 x 9
Back cover 'Seeking redemption on the Via de la Plata.
Owen Tessary’s life changed forever in a moment of madness. Haunted by his crime, Owen feels a calling to seek redemption on the Camino de Santiago.
The daily toil of walking the Via de la Plata from Seville causes Owen to search his soul.
On The Way Owen encounters other pilgrims with their own personal reasons to answer the call of the camino.
Join Owen for the many highs and lows of camino life as he moves step by step closer to his goal.
Can the Camino give Owen peace of mind and stop his nightmares?'
Overall vision 'The front cover at the top should be the title:
Camino
Calling
This will fill about 20 per cent of the front cover. It must be centre justified. The title should use the same type face as the official Camino de Santiago road sign (see first download). The type should be in bright blue. The background should be in bright yellow.
Under the title should be an image of a path stretching to the horizon with the shadow of a pilgrim (see second download).
Superimposed on the image should be the words 'a Owen Tessary novel' maybe using a type face similar to the street signage used in Spain (see third download).
At the bottom of the front cover should be the author's name 'Karl Dunmore' in the same style as the blue and yellow title - BUT MUCH SMALLER.
On the SPINE of the book should be 'Harbour Lantern' and 'Karl Dunmore' in the blue text on yellow background.
On the back cover there should be a photograph (see fourth download) with the text UPDATE ON THE TEXT 'Seeking redemption on the Via de la Plata.
In a moment of madness Owen Tessary’s life changed forever. Haunted by his atrocious act, he feels a calling to seek redemption on the Camino de Santiago.
The daily slog of walking the Via de la Plata from Seville causes Owen to search deep within his soul.
On The Way Owen encounters other pilgrims with their own personal reasons to answer the call of the Camino.
Can the Camino give Owen peace of mind and stop his nightmares?' with a three centimetre space at the bottom for bar code/ISBN and the author headshot photograph attached.
Updates

Target Market(s)

Readers who have walked the Camino de Santiago in Spain or who are interested

Requirements
Nice to have
• I would like my headshot (attached) included on the back cover

```html
<!DOCTYPE html>
<html lang="en">
<head>
<meta charset="utf-8">
<title>Harbour Lantern — book cover</title>
<link rel="stylesheet" href="https://fonts.googleapis.com/css2?family=Londrina+Solid:wght@900&family=Barlow+Semi+Condensed:wght@300;500&display=swap">
<style>
  :root {
    --stage: #000000;
    --sky-blue: #00aeef;
    --teal: #2fbac6;
    --meadow: #8bd170;
    --sun-yellow: #fff200;
    --paper-white: #ffffff;
    --author-blue: #29a8e0;
  }
  html, body {
    margin: 0;
    padding: 0;
    width: 1200px;
    height: 1200px;
    overflow: hidden;
    background: var(--stage);
  }
  .canvas {
    position: relative;
    width: 1200px;
    height: 1200px;
    background: var(--stage);
  }
  .cover {
    position: absolute;
    left: 230px;
    top: 44px;
    width: 741px;
    height: 1112px;
    overflow: hidden;
    background: linear-gradient(180deg,
      var(--sky-blue) 0%,
      var(--sky-blue) 30%,
      var(--teal) 48%,
      var(--meadow) 68%,
      #c6e33a 86%,
      var(--sun-yellow) 100%);
  }
  .title {
    position: absolute;
    left: 0;
    right: 0;
    top: 48px;
    margin: 0;
    text-align: center;
    font-family: "Londrina Solid", "Arial Narrow", sans-serif;
    font-weight: 900;
    font-size: 176px;
    line-height: 182px;
    letter-spacing: 2px;
    color: var(--paper-white);
    text-transform: uppercase;
  }
  .title span { display: block; }
  .series-line {
    position: absolute;
    left: 0;
    right: 0;
    top: 478px;
    margin: 0;
    text-align: center;
    font-family: "Barlow Semi Condensed", "Arial Narrow", sans-serif;
    font-weight: 300;
    font-size: 44px;
    color: var(--paper-white);
  }
  .pilgrim-path {
    position: absolute;
    left: 148px;
    top: 520px;
    width: 444px;
    height: 592px;
    background: radial-gradient(ellipse 22% 100% at 50% 100%,
      rgba(255,255,255,0.95) 0%,
      rgba(255,255,255,0.75) 55%,
      rgba(255,255,255,0) 100%);
  }
  .author {
    position: absolute;
    left: 0;
    right: 0;
    top: 1006px;
    margin: 0;
    text-align: center;
    font-family: "Barlow Semi Condensed", "Arial Narrow", sans-serif;
    font-weight: 500;
    font-size: 52px;
    color: var(--author-blue);
  }
</style>
</head>
<body>
  <div class="canvas">
    <div class="cover">
      <h1 class="title"><span>Harbour</span><span>Lantern</span></h1>
      <p class="series-line">a Owen Tessary novel</p>
      <div class="pilgrim-path" role="img" aria-label="White silhouette of a pilgrim's long shadow stretching down a speckled path"></div>
      <p class="author">K L Dunmore</p>
    </div>
  </div>
</body>
</html>
```